Harwick Physiotherapy needs a brochure that will highlight and sell our services to prospective clie

Harwick Physiotherapy. The treatment you need , the care you deserve.

We need a brochure design for our musculoskeletal physiotherapy business. It needs to sell our service to prospective clients and to referrers and communicate our values and mission. It needs to incorporate our services of: back and neck pain, muscle and joint sprains and strains, sports injury management, including video assessment, acupuncture, Pilates, women's health/pelvic floor physio, deep tissue massage. We use technology including video analysis to improve patient outcomes. Our website is http://harwickphysio.co.nz attached are some images from web site and some graphics including our logo

Ideally a front page with our logo and graphics and bulletin points of our services

Sports Injuries
Back , neck and joint pain
Orthopedic rehabilitation
Acupuncture
Pelvic floor Physiotherapy

Then inside our USP's why us (see our web site) plus ....
We provide expert diagnosis of your problem and committed/dedicated to providing the best possible solution to get you back to what you love and improve your performance
Also we specialise in the use of technology with video analysis (http://www.strivelens.com/), digital postural analysis software (http://alignmetrix.com/mobile/), computer graphics for education (http://applications.anatovista.com/shoulder_pro) and video/online exercise programs (https://www.kinetrova.org/index.php), online booking (http://nzappts.bookrally.com/harwick/)
Long appointments , not rushed , to give us time to help

Then sections for:

Physiotherapy
sports physio
Orthopaedic rehab
back and neck pain
acupuncture
women's health inside
take info from our website, but also I can upload brochures from Rehab Guild NZ, take the best out of each of those and combine with our web info to provide description for each.

And on back all contact detail and QR code for our website

Target Market(s)

mostly 40 to 60 comfortably off, educated, active, some sporty, healthy, middle class

Industry/Entity Type

Education

Requirements
Must have
• Must match our website with the logo and pictures on home page
brochure to be A4 trifold DLE, please match our font or use one we can use easily
Nice to have
• not too busy, give our customers good reasons to use our services,

```html
<!DOCTYPE html>
<html lang="en">
<head>
<meta charset="utf-8">
<title>Harwick Physiotherapy – Trifold Inside</title>
<link href="https://fonts.googleapis.com/css2?family=Arimo:ital,wght@0,400;0,700;1,400;1,700&family=Lora:ital,wght@1,400;1,700&display=swap" rel="stylesheet">
<style>
:root{
  --orange:#f07d22;
  --ink:#222;
  --heading:#454c55;
  --slate:#46525a;
  --page:#fff;
  --backdrop:#e6e6e6;
}
*{box-sizing:border-box;margin:0;padding:0}
html,body{width:1200px;height:891px;overflow:hidden;background:var(--backdrop)}
body{font-family:"Arimo",Arial,sans-serif;color:var(--ink);position:relative}
.sheet{position:absolute;left:78px;top:42px;width:1027px;height:796px;background:var(--page);box-shadow:0 1px 4px rgba(0,0,0,.25);overflow:hidden}
.abs{position:absolute}
.section-title{position:absolute;display:flex;align-items:center;font-weight:700;font-size:18px;color:var(--heading);height:28px}
.section-title::before{content:"";width:17px;height:28px;background:var(--orange);border-radius:2px 8px 2px 2px;margin-right:6px}
.body{font-size:12.6px;line-height:15.6px;text-align:justify}
.subhead{font-family:"Lora",Georgia,serif;font-style:italic;font-weight:700;font-size:14px;color:#2f3a4a;line-height:17px}
.subhead em{color:var(--orange);font-style:italic}
.band{position:absolute;height:26px;background:var(--orange);border-radius:6px;color:#fff;font-family:"Lora",Georgia,serif;font-style:italic;font-weight:700;font-size:15px;display:flex;align-items:center;justify-content:center}
.bullets{list-style:none;font-size:13px}
.bullets li{position:relative;padding-left:14px}
.bullets li::before{content:"";position:absolute;left:0;top:5px;width:7px;height:7px;border-radius:50%;background:var(--orange)}
.photo{position:absolute}
.highlight{color:var(--orange);font-weight:700}
.promo{font-family:"Lora",Georgia,serif;font-style:italic;font-size:13px;line-height:15.5px;text-align:center}
.web-button{position:absolute;background:var(--slate);color:#fff;border-radius:7px;font-size:15px;display:flex;align-items:center;justify-content:center;letter-spacing:.3px}
.guarantee-text{position:absolute;color:#fff;font-style:italic;font-weight:700;font-size:14.5px;line-height:20px}
.guarantee-seal{position:absolute;border:2px solid #fff;border-radius:50%;color:#fff;font-size:12.5px;font-weight:700;text-align:center;display:flex;align-items:center;justify-content:center;line-height:16px}
</style>
</head>
<body>
<main class="sheet">

  <!-- Panel: Physiotherapy -->
  <section class="panel panel-physio">
    <h2 class="section-title" style="left:100px;top:21px">Physiotherapy</h2>
    <div class="abs" style="left:23px;top:64px;width:305px">
      <h3 class="subhead">Injury <em>Management</em> and <em>Rehabilitation</em></h3>
      <p class="body">Whether your a weekend warrior, a professional athlete, have muscle, joint or spinal pain or have had orthopedic surgery – a physiotherapist can help get you moving again and back on the field sooner.</p>
      <h3 class="subhead" style="margin-top:2px">Injury <em>Prevention</em></h3>
      <p class="body">You don't need to wait for an injury to seek advice; you can also see your physio for help to prevent injuries and enhance your sport performance.</p>
      <h3 class="subhead" style="margin-top:2px">Orthopedic <em>Rehab</em></h3>
      <p class="body">If you are planning surgery or are recovering afterwards, then your physiotherapist can help you with evidence based methods to help you prepare or recover your mobility and strength.</p>
    </div>
    <div class="band" style="left:21px;top:298px;width:307px">Your Physiotherapists May Offer You:</div>
    <div class="photo" role="img" aria-label="Couple jogging along a sunny beach" style="left:150px;top:365px;width:197px;height:300px;background:linear-gradient(180deg,#eaf2f5 0%,#cfe2ea 35%,#e9d9c3 65%,#e6d2b8 100%)"></div>
    <ul class="bullets abs" style="left:32px;top:334px;line-height:19.9px">
      <li>Deep tissue, sports &amp; therapeutic massage</li>
      <li>Joint/Spinal mobilisation &amp; manipulation</li>
      <li>Muscle Energy Techniques</li>
      <li>Exercise prescription</li>
      <li>Trigger point release</li>
      <li>Orthotic prescription</li>
      <li>Muscle stretching</li>
      <li>Tendon stretching</li>
      <li>Postural Analysis</li>
      <li>Lifestyle advice</li>
      <li>Taping or braces</li>
      <li>Electrotherapy</li>
      <li>Acupuncture</li>
      <li>Dry Needling</li>
      <li>Pilates</li>
    </ul>
  </section>

  <!-- Panel: Acupuncture & Women's Health -->
  <section class="panel panel-middle">
    <h2 class="section-title" style="left:447px;top:21px">Acupuncture</h2>
    <p class="body abs" style="left:363px;top:64px;width:308px">Acupuncture can have a powerful and sustained effect on pain and dysfunction in the body – as the process can stimulate natural pain relieving and healing mechanisms in the body. It is often used to treat: • Acute and chronic injuries • Back and neck pain • Muscle and joint problems • Nerve pain • Arthritis • Headaches and migraines • Sports injuries</p>

    <h2 class="section-title" style="left:431px;top:198px">Women's Health</h2>
    <div class="abs" style="left:363px;top:239px;width:308px">
      <h3 class="subhead" style="text-align:center;font-size:14.5px;margin-bottom:8px">What can create Pelvic Floor Problems?</h3>
      <p class="body">Pregnancy, menopause, gynecological procedures and a history of back pain or pelvic pain can all lead to either pelvic floor weakness or dysfunction. Other risk factors include being overweight, a chronic cough or sneeze along with repeat heavy lifting.</p>
      <p class="body" style="margin-top:8px">If you are experiencing any issues or are just interested in learning how to care for your pelvic floor please call to make an appointment with our pelvic health physiotherapist who will be able to put together <span class="highlight">an appropriate personalised program for You.</span></p>
    </div>
    <p class="promo abs" style="left:364px;top:458px;width:160px">Visit our website for the FREE “Pelvic floor screening test” and “Bladder diary” that will help you figure out if you are at risk of pelvic floor problems.</p>
    <div class="photo" role="img" aria-label="Torso wrapped in a sarong holding pink lilies" style="left:530px;top:443px;width:140px;height:140px;border-radius:50%;border:3px solid var(--orange);background:radial-gradient(circle at 55% 50%,#f4c9c2 0%,#f2dcd3 40%,#bcd9e6 75%,#f5f1ee 100%)"></div>
    <div class="web-button" style="left:373px;top:612px;width:287px;height:35px">harwickphysio.co.nz</div>
  </section>

  <!-- Guarantee band -->
  <svg class="abs" style="left:0;top:650px" width="687" height="146" viewBox="0 0 687 146" aria-hidden="true">
    <path d="M0 30 C 180 0, 420 10, 687 36 L687 146 L0 146 Z" fill="#f07d22"/>
    <path d="M0 22 C 180 -6, 420 4, 687 30" fill="none" stroke="#f07d22" stroke-width="2"/>
  </svg>
  <div class="guarantee-seal" style="left:50px;top:683px;width:104px;height:104px">OUR<br>GUARANTEE</div>
  <div class="guarantee-text" style="left:184px;top:695px">
    <p>If for any reason you are not 100% satisfied with the level of<br>service you receive we will:</p>
    <p style="font-style:normal;font-size:15px">• Give you a FULL REFUND of your appointment charge AND</p>
    <p style="font-style:normal;font-size:15px">• There will be NO CHARGE for your next appointment</p>
  </div>

  <!-- Panel: Back and neck pain -->
  <section class="panel panel-back">
    <h2 class="section-title" style="left:754px;top:21px">Back and neck pain</h2>
    <p class="body abs" style="left:703px;top:64px;width:304px">Over 80% of New Zealanders experience some form of back pain. If you're one of them, then you know what a struggle it can be. If you're searching for a solution to treat your back pain and prevent future problems then physiotherapy can help you.</p>
    <div class="band" style="left:704px;top:154px;width:304px">Your Physio Can Help with:</div>
    <ul class="bullets abs" style="left:722px;top:191px;width:282px;line-height:15.5px">
      <li style="margin-bottom:5px">Assessment and advice on your back pain</li>
      <li style="margin-bottom:5px">Mobilisation and manipulation as appropriate</li>
      <li style="margin-bottom:5px">Specific strengthening and flexibility exercises</li>
      <li style="margin-bottom:5px">Designing a pain management plan</li>
      <li style="margin-bottom:5px">Exercises to improve your posture</li>
      <li style="margin-bottom:5px">Improving sports performance</li>
      <li style="margin-bottom:5px">Education on how to help prevent future back problems</li>
      <li style="margin-bottom:5px">Advice on returning to work, sport and general activities</li>
      <li style="margin-bottom:5px">Workstation assessments, ergonomic analysis and advice on specific work tasks</li>
      <li>Referring you to other appropriate health providers (specialists or GPs) if needed.</li>
    </ul>
    <div class="photo" role="img" aria-label="Grandparents carrying two young grandchildren on the beach" style="left:687px;top:458px;width:340px;height:338px;background:linear-gradient(180deg,#ffffff 0%,#dbeaf2 25%,#7fb0cb 50%,#bcd4de 70%,#e2d6c4 100%)"></div>
  </section>

</main>
</body>
</html>
```